Harwick Structure Works needs a Business card design and logo

We Need a business card design and logo for a Building & Construction business based in Melbourne. We work in both the Domestic & Commercial sector. We specialize in all aspects of building including extensions, Renovations, and alterations. Construction Management, Project Management, And labour hire

Industry/Entity Type

Business

```html
<!DOCTYPE html>
<html lang="en">
<head>
<meta charset="utf-8">
<title>Harwick Structure Works – Business Card</title>
<link rel="stylesheet" href="https://fonts.googleapis.com/css2?family=Source+Sans+3:wght@400;600&display=swap">
<style>
  :root {
    --backdrop: #8f8f8f;
    --card-white: #ffffff;
    --card-tint: #f1f2f6;
    --navy: #163a64;
    --navy-deep: #10304f;
    --red: #e2262d;
    --text-white: #ffffff;
    --faint: #e4e6ee;
  }
  * { box-sizing: border-box; margin: 0; padding: 0; }
  html, body {
    width: 1200px;
    height: 900px;
    overflow: hidden;
    background: var(--backdrop);
    font-family: "Source Sans 3", "Myriad Pro", Arial, sans-serif;
  }
  .canvas {
    position: relative;
    width: 1200px;
    height: 900px;
    display: flex;
    align-items: center;
    justify-content: center;
    gap: 40px;
  }
  .card {
    position: relative;
    width: 540px;
    height: 310px;
    border-radius: 18px;
    overflow: hidden;
    background: linear-gradient(180deg, var(--card-white) 0%, var(--card-tint) 100%);
    box-shadow: 0 10px 24px rgba(0,0,0,0.22);
  }
  .card__backdrop {
    position: absolute;
    top: 0;
    right: 0;
    width: 220px;
    height: 100%;
    background: linear-gradient(180deg, rgba(228,230,238,0) 0%, var(--faint) 60%, rgba(228,230,238,0.6) 100%);
  }
  .brand {
    position: absolute;
    display: flex;
    align-items: center;
    gap: 12px;
  }
  .brand__square {
    width: 34px;
    height: 34px;
    background: var(--navy);
    flex-shrink: 0;
  }
  .brand__name {
    color: var(--navy);
    font-weight: 600;
    font-size: 30px;
    line-height: 1.02;
  }
  .band {
    position: absolute;
    left: 0;
    right: 0;
    bottom: 0;
    background: var(--navy);
    border-top: 4px solid var(--red);
    box-shadow: 0 -6px 0 var(--card-white), 0 -8px 0 var(--red);
  }
  /* front */
  .card--front .brand { left: 40px; top: 110px; }
  .card--front .band { height: 66px; }
  .services {
    display: flex;
    align-items: center;
    height: 100%;
    padding: 0 18px;
    list-style: none;
  }
  .services__item {
    color: var(--text-white);
    font-size: 19px;
    padding: 0 11px;
    border-left: 1.5px solid var(--text-white);
    line-height: 1.3;
  }
  .services__item:first-child { border-left: none; padding-left: 4px; }
  /* back */
  .card--back .brand { left: 40px; top: 56px; }
  .card--back .band { height: 152px; }
  .holder {
    position: absolute;
    right: 22px;
    top: 12px;
    text-align: right;
  }
  .holder__name { color: var(--red); font-size: 19px; line-height: 1.1; }
  .holder__role { color: var(--text-white); font-size: 15px; }
  .contacts {
    position: absolute;
    left: 26px;
    bottom: 24px;
    list-style: none;
  }
  .contacts__row {
    color: var(--text-white);
    font-size: 18px;
    line-height: 1.15;
  }
  .contacts__label { color: var(--red); }
</style>
</head>
<body>
  <main class="canvas">
    <section class="card card--front">
      <div class="card__backdrop" role="img" aria-label="Faint construction site backdrop"></div>
      <div class="brand">
        <span class="brand__square"></span>
        <span class="brand__name">Harwick<br>Structure Works</span>
      </div>
      <div class="band">
        <ul class="services">
          <li class="services__item">Extentions</li>
          <li class="services__item">Renovations</li>
          <li class="services__item">Alterations</li>
          <li class="services__item">pargolas</li>
          <li class="services__item">Decks</li>
        </ul>
      </div>
    </section>

    <section class="card card--back">
      <div class="card__backdrop" role="img" aria-label="Faint construction site backdrop"></div>
      <div class="brand">
        <span class="brand__square"></span>
        <span class="brand__name">Harwick<br>Structure Works</span>
      </div>
      <div class="band">
        <div class="holder">
          <p class="holder__name">Dana Harwick</p>
          <p class="holder__role">Dsignation</p>
        </div>
        <ul class="contacts">
          <li class="contacts__row"><span class="contacts__label">Mobile:</span> 0400 555 018</li>
          <li class="contacts__row"><span class="contacts__label">Office:</span> (03) 9000 4127</li>
          <li class="contacts__row"><span class="contacts__label">Email:</span> info@harwickstructure.com.au</li>
        </ul>
      </div>
    </section>
  </main>
</body>
</html>
```